Willow Dental Business Card

We need business cards for our dental office.
We are looking for a clean, elegant design

We provide dental services to children.
Our card needs to be appealing to referring dentists, parents and our team

Target Market(s)

referring dentists, parents and our team

Industry/Entity Type

Dental Clinic

Contact Information for Business Card

4856 Fenwick Lane, Suite 100
Middleburg Heights, OH 44187

216-382-7461 Voice
216-382-7469 fax
info@willowdentalco.com email
www.willowdentalco.com web

Font styles to use
Sans Serif

Requirements
Must have
• White background - clean, crisp, elegant, simple
• rounded corners
• different color palate - once we come up with design, we will replace the blue with orange, green,
Nice to have
• Follow our logo typeface and colors
• then we can replace color

```html
<!DOCTYPE html>
<html lang="en">
<head>
<meta charset="utf-8">
<title>Willow Dental Business Card</title>
<link href="https://fonts.googleapis.com/css2?family=Varela+Round&display=swap" rel="stylesheet">
<style>
  :root {
    --brand-blue: #0ea0dc;
    --brand-blue-deep: #0893cf;
    --ink-grey: #6f6f6f;
    --rule-grey: #a9a9a9;
    --card-white: #f7f7f7;
    --backdrop: #3a3a3a;
  }
  * { margin: 0; padding: 0; box-sizing: border-box; }
  html, body { width: 1200px; height: 1021px; overflow: hidden; }
  body {
    background: var(--backdrop);
    font-family: "Varela Round", sans-serif;
    position: relative;
  }
  .card {
    position: absolute;
    width: 640px;
    height: 366px;
    border-radius: 28px;
    box-shadow: 0 14px 30px rgba(0,0,0,0.35);
  }
  .card-back {
    left: 420px;
    top: 90px;
    background: linear-gradient(160deg, var(--brand-blue) 0%, var(--brand-blue-deep) 100%);
    display: flex;
    align-items: center;
    justify-content: center;
  }
  .card-back .wordmark {
    color: #ffffff;
    font-size: 46px;
    letter-spacing: 0.5px;
  }
  .card-front {
    left: 140px;
    top: 520px;
    background: var(--card-white);
  }
  .front-wordmark {
    position: absolute;
    left: 40px;
    top: 120px;
    color: var(--brand-blue);
    font-size: 38px;
    letter-spacing: 0.3px;
  }
  .divider {
    position: absolute;
    left: 326px;
    width: 2px;
  }
  .divider-accent { top: 78px; height: 40px; background: var(--brand-blue); }
  .divider-main { top: 132px; height: 100px; background: var(--rule-grey); }
  .person {
    position: absolute;
    left: 360px;
    top: 78px;
  }
  .person-name {
    color: var(--brand-blue);
    font-size: 24px;
    font-weight: 700;
    letter-spacing: 0.5px;
  }
  .person-title {
    color: var(--ink-grey);
    font-size: 17px;
    margin-top: 2px;
  }
  .contact-list {
    position: absolute;
    left: 360px;
    top: 152px;
    list-style: none;
    color: var(--ink-grey);
    font-size: 17px;
    line-height: 25px;
  }
  .contact-list li { display: flex; align-items: center; gap: 8px; }
  .contact-list svg { width: 15px; height: 15px; fill: var(--brand-blue); flex: none; }
  .address {
    position: absolute;
    left: 40px;
    right: 40px;
    bottom: 44px;
    color: var(--ink-grey);
    font-size: 17.5px;
    letter-spacing: 0.2px;
  }
</style>
</head>
<body>

<section class="card card-back">
  <span class="wordmark">Willow Dental</span>
</section>

<section class="card card-front">
  <span class="front-wordmark">Willow Dental</span>

  <span class="divider divider-accent"></span>
  <span class="divider divider-main"></span>

  <div class="person">
    <div class="person-name">Daniel Hartley</div>
    <div class="person-title">President</div>
  </div>

  <ul class="contact-list">
    <li>
      <svg viewBox="0 0 16 16" aria-hidden="true"><path d="M3.6 1.2l2.3 2.6-1.3 2c.9 1.9 2.5 3.5 4.4 4.4l2-1.3 2.6 2.3-1.2 2.3C7 14.6 1.4 9 .9 3.7z"/></svg>
      216-382-7461
    </li>
    <li>
      <svg viewBox="0 0 16 16" aria-hidden="true"><path d="M4 1h8v4H4zM1 6h14v6h-3v3H4v-3H1zm4 4v4h6v-4z"/></svg>
      216-382-7469
    </li>
    <li>
      <svg viewBox="0 0 16 16" aria-hidden="true"><path d="M1 3h14v10H1zm1.5 1.2v.4L8 8.8l5.5-4.2v-.4zm0 2.2v5.4h11V6.4L8 10.6z"/></svg>
      info@willowdentalco.com
    </li>
    <li>
      <svg viewBox="0 0 16 16" aria-hidden="true"><path d="M8 1a7 7 0 100 14A7 7 0 008 1zm0 1.4c.9 0 1.8 1.5 2.1 4H5.9C6.2 3.9 7.1 2.4 8 2.4zM2.5 7.4h2.1c0-.3 0 .9 0 1.2H2.5zm0 0c.2-2.2 1.7-4 3.7-4.7-.6 1-1 2.4-1.1 4.7zm3.4 1.2h4.2c-.3 2.5-1.2 4-2.1 4s-1.8-1.5-2.1-4zm5.5-1.2c-.1-2.3-.5-3.7-1.1-4.7 2 .7 3.5 2.5 3.7 4.7zm0 1.2h2.1c-.2 2.2-1.7 4-3.7 4.7.6-1 1-2.4 1.6-4.7zm-6.8 0c.1 2.3.5 3.7 1.1 4.7-2-.7-3.5-2.5-3.7-4.7z"/></svg>
      www.willowdentalco.com
    </li>
  </ul>

  <div class="address">4856 Fenwick Lane, Suite 100, Middleburg Heights, OH 44187</div>
</section>

</body>
</html>
```